Swimming Pool Service business card needed!!!! Please

Hi Everyone! Thanks for looking at my contest. I PROMISE to provide excellent feedback during this process.

I am starting a new swimming pool cleaning business in San Diego, California and would like your help in making a business card for me.

I like easy to read, classy and sophisticated.

I am having a website designed and I'm looking for it to have pictures of really clean & clear pools.

I really like the blue on white color format, but open to other colors.

I do not have a logo, but the name of my company is GLIMMERTIDE POOL SERVICE.

My tag line is: Pools so clean, you can see yourself "in" them. (does not need to have the quotes around "in"...maybe just italics for this word IN?) You decide for me.

I would like to have a logo designed that incorporates some sort of easy to read letters. I do not want cursive (handwriting) letters. I thought about having a "reflection" of letters (mirror image), but think that this will be hard to read from far away. Maybe you can surprise me and come up with an idea that works using the a mirror image....but I'm not sure. I was leaning toward plain old BLOCK letters as I think it would be easy to read on my truck.

I would like to have the NAQTR and WBK logos on the back of the card. I have attached those two as files. You can put other things on the back as well, but I need these two logos on there. Or maybe put them on the front of the card if you have a better idea for the back of the card! :-)

Maybe blue on the back of the card and white on the front of the card? I don't know, I'm just thinking out loud.

I had another card done awhile ago called HARBORLINE TEES. I have uploaded a copy of that card for your reference. I don't want this card to be the same as my new company is a swimming pool cleaning company, but I wanted you to see what I liked in the past.

THANK YOU!!!!
Updates

Reason: Partner out of town and want their feedback....so need more time to decide and designs still coming in.

Industry/Entity Type

Business

Contact Information for Business Card

GLIMMERTIDE POOL SERVICE
Dale Wexby
Owner
4817 Quarry Bend Ave. #512
San Diego, CA 92417
858-291-6083
www.glimmertidepoolservice.example

Font styles to use
Sans Serif

Colors
0255a3
3176b5
ffffff

Requirements
Nice to have
• Some things to (possibly) add to back of card (in no particular order)
• WBK logo
• NAQTR logo
• Free Estimates
• Residential and Commercial Services
• Equipment Repairs
• Saltwater Systems
• Licensed, Bonded, Insured
• Family Owned and Operated
• No Contracts
• =======================
• Check out the FolioMint business card that i attached.
• i think they did this using a chrome overlay.
• Can any of you guys design that? or is that done at my printer?
• ==================
Should not have
• Hi Designers-
• The first round of cards came back and let's stay away from the light blue (powder blue) color. I don't like the look of it on the business cards.
• Also, the pool company JPG's that I attached are other logos of pool companies that I liked. I don't want them to be on my card. The only logos that should be on my card are the one you are going to come up with for my company, the WBK logo and the NAQTR logo.
• Lastly, no vertical cards and no split cards (logo on left, contact info on right side).
• Thanks much!

```html
<!DOCTYPE html>
<html lang="en">
<head>
<meta charset="utf-8">
<title>Glimmertide Pool Service – Business Card</title>
<link rel="stylesheet" href="https://fonts.googleapis.com/css2?family=Ubuntu:wght@400;500&family=PT+Sans:ital,wght@0,700;1,700&display=swap">
<style>
  :root {
    --canvas: #ffffff;
    --card-tan: #a8795b;
    --blue-deep: #1b59a3;
    --blue-mid: #3176b5;
  }
  * { box-sizing: border-box; margin: 0; padding: 0; }
  html, body {
    width: 1100px; height: 1200px; overflow: hidden;
    background: var(--canvas);
  }
  .sheet { position: relative; width: 1100px; height: 1200px; }

  .card {
    position: absolute;
    width: 899px; height: 529px;
    background: var(--card-tan);
    overflow: hidden;
  }
  .card--front { left: 0; top: 91px; }
  .card--back  { left: 3px; top: 668px; }

  .stripe {
    position: absolute;
    background: var(--blue-deep);
  }
  .stripe::after {
    content: ""; position: absolute; background: var(--blue-mid);
  }
  .stripe--vertical { left: 62px; top: 0; width: 33px; height: 100%; }
  .stripe--vertical::after { left: 10px; top: 0; width: 12px; height: 100%; }
  .stripe--horizontal { left: 0; top: 447px; width: 100%; height: 33px; }
  .stripe--horizontal::after { left: 0; top: 10px; width: 100%; height: 11px; }

  .brand {
    position: absolute;
    display: flex; align-items: center; gap: 14px;
    font-family: "Ubuntu", sans-serif;
    font-weight: 500;
    color: var(--blue-deep);
    letter-spacing: 0.04em;
    white-space: nowrap;
  }
  .brand__dot {
    flex: none; border-radius: 50%; background: var(--blue-deep);
  }
  .card--front .brand {
    left: 0; width: 100%; justify-content: center; padding-left: 90px;
    top: 215px; font-size: 44px;
  }
  .card--front .brand__dot { width: 34px; height: 34px; }
  .card--back .brand {
    left: 0; width: 100%; justify-content: center; padding-left: 60px;
    top: 82px; font-size: 21px; gap: 8px;
  }
  .card--back .brand__dot { width: 16px; height: 16px; }

  .tagline {
    position: absolute; left: 0; width: 100%; top: 150px;
    padding-left: 88px;
    display: flex; justify-content: center;
    white-space: nowrap;
  }
  .tagline__text {
    display: inline-block;
    font-family: "Ubuntu", sans-serif;
    font-weight: 400;
    font-size: 52px;
    line-height: 60px;
    color: var(--blue-mid);
    transform: scaleX(0.68);
    transform-origin: center;
  }
  .tagline__text em {
    font-weight: 500; font-style: italic;
    color: var(--blue-deep);
  }

  .contact {
    position: absolute; left: 0; width: 100%;
    font-family: "PT Sans", sans-serif; font-weight: 700;
    text-align: center;
  }
  .contact__name {
    top: 244px; font-size: 34px; color: var(--blue-deep);
    padding-left: 32px;
  }
  .contact__role {
    top: 281px; font-size: 22px; color: var(--blue-mid);
    padding-left: 22px;
  }
  .contact__details {
    top: 328px; font-size: 25px; line-height: 28px; color: var(--blue-deep);
    padding-left: 72px;
  }
</style>
</head>
<body>
<main class="sheet">

  <section class="card card--front" aria-label="Card front">
    <div class="stripe stripe--vertical"></div>
    <div class="stripe stripe--horizontal"></div>
    <div class="brand"><span class="brand__dot"></span>GLIMMERTIDE POOL SERVICE</div>
  </section>

  <section class="card card--back" aria-label="Card back">
    <div class="stripe stripe--vertical"></div>
    <div class="stripe stripe--horizontal"></div>
    <div class="brand"><span class="brand__dot"></span>GLIMMERTIDE POOL SERVICE</div>

    <p class="tagline"><span class="tagline__text">Pools so clean, you can see yourself <em>in</em> them.</span></p>

    <p class="contact contact__name">Dale Wexby</p>
    <p class="contact contact__role">Owner</p>
    <p class="contact contact__details">
      4817 Quarry Bend Ave.<br>
      #512 San Diego, CA 92417<br>
      Phone : 858-291-6083<br>
      www.glimmertidepoolservice.example
    </p>
  </section>

</main>
</body>
</html>
```